Web Design for Cloud Software Solution for Oil Field

Web Design for Company that created software for field data gathering and workflow automation solution built for realization of digital oilfield for all companies for efficient & safe production of energy of the future. Company mission is to connect every field equipment and worker including back office to provide a seamless connected field operation. Reduce operational spending without upfront capital investment. Provide self-learning digital solutions at every step of the way assisting. Goal is to get visitor to schedule a demo.

Target Market(s)

Old Field Operators, Operations managers

Coding

Coded - Design and coding required

Font styles to use
Sans Serif

Colors
0255a3
acd036
1b1b1b
eaeaea

Requirements
Must have
• Slider, testimonial section

```html
<!DOCTYPE html>
<html lang="en">
<head>
<meta charset="utf-8">
<title>Norvane – Cloud Software Solutions for Oilfield</title>
<link rel="stylesheet" href="https://fonts.googleapis.com/css2?family=Montserrat:wght@400;500;600;700&family=Open+Sans:ital,wght@0,400;0,600;1,400&display=swap">
<style>
:root{
  --blue:#0255a3;
  --navy:#0a2a6b;
  --green:#acd036;
  --green-deep:#7fb02a;
  --ink:#1b1b1b;
  --grey:#eaeaea;
  --text:#555;
  --white:#fff;
}
*{box-sizing:border-box;margin:0;padding:0}
html,body{width:1200px;height:3422px;overflow:hidden}
body{font-family:"Open Sans",Arial,sans-serif;color:var(--text);background:var(--white);position:relative}
.heading{font-family:"Montserrat",Arial,sans-serif;font-weight:700}

/* Hero */
.hero{position:absolute;left:0;top:0;width:1200px;height:598px}
.hero-photo{position:absolute;inset:0;background:linear-gradient(180deg,#4d4a78 0%,#8a6a86 35%,#b8765a 60%,#3e3a48 100%)}
.hero-shade{position:absolute;inset:0;background:linear-gradient(90deg,rgba(20,20,40,.45),rgba(20,20,40,.1))}
.topbar{position:absolute;right:96px;top:24px;display:flex;gap:14px;align-items:center;font-family:"Montserrat",sans-serif;font-size:16px;color:var(--white)}
.topbar span{display:flex;align-items:center;gap:8px}
.topbar .sep{width:1px;height:16px;background:rgba(255,255,255,.7)}
.brand{position:absolute;left:100px;top:52px;font-family:"Montserrat",sans-serif;font-weight:700;font-size:35px;color:var(--white);letter-spacing:1px}
.nav{position:absolute;left:383px;top:72px;display:flex;gap:30px;align-items:center;font-family:"Montserrat",sans-serif;font-weight:500;font-size:16px;color:var(--white)}
.nav .active{color:var(--green)}
.hero-title{position:absolute;left:100px;top:176px;font-size:48px;line-height:68px;color:var(--white);letter-spacing:1px}
.btn-demo{position:absolute;left:100px;top:411px;width:200px;height:56px;border-radius:28px;background:var(--green);color:var(--white);font-family:"Montserrat",sans-serif;font-weight:700;font-size:15px;display:flex;align-items:center;justify-content:center}
.slider-dots{position:absolute;left:568px;top:534px;display:flex;gap:5px}
.slider-dots i{width:11px;height:11px;border-radius:50%;border:1.5px solid var(--white)}
.slider-dots i.on{background:var(--white)}

/* Mission */
.section-title{font-size:33px;color:var(--blue);text-align:center;position:absolute;left:0;width:1200px}
.mission-title{top:662px}
.mission-text{position:absolute;left:285px;width:630px;top:728px;text-align:center;font-size:14px;line-height:27px}
.video{position:absolute;left:399px;top:849px;width:402px;height:257px;border:3px solid var(--grey);box-shadow:0 1px 4px rgba(0,0,0,.15)}
.video-still{position:absolute;inset:0;background:linear-gradient(180deg,#b9a0b8 0%,#e3a7a0 45%,#5a6f93 62%,#253c66 100%)}
.play{position:absolute;left:50%;top:50%;transform:translate(-50%,-50%)}

/* Industry */
.industry{position:absolute;left:0;top:1195px;width:1200px;height:482px}
.industry-panel{position:absolute;left:0;top:0;width:598px;height:482px;background:var(--blue)}
.industry-photo{position:absolute;left:598px;top:0;width:602px;height:482px;background:linear-gradient(180deg,#e8d2be 0%,#cdb8a4 45%,#6f6a66 80%,#3f3f45 100%)}
.industry h2{position:absolute;left:98px;top:50px;font-size:33px;color:var(--white)}
.industry p{position:absolute;left:100px;top:112px;width:452px;font-size:13.5px;line-height:25px;color:var(--white)}
.btn-outline{position:absolute;left:100px;top:370px;width:131px;height:48px;border:2px solid var(--white);border-radius:24px;color:var(--white);font-family:"Montserrat",sans-serif;font-weight:700;font-size:13px;display:flex;align-items:center;justify-content:center}

/* Technology */
.tech-title{top:1752px;color:var(--navy)}
.tech-text{position:absolute;left:130px;width:940px;top:1818px;text-align:center;font-size:13.5px;line-height:27px}
.diagram{position:absolute;left:0;top:0}
.diagram text{font-family:Arial,sans-serif;font-size:15.5px;fill:var(--ink)}

/* Testimonials */
.testimonials{position:absolute;left:0;top:2519px;width:1200px;height:488px;background:linear-gradient(135deg,#9cc233 0%,#86b02b 50%,#9dc435 100%)}
.testimonials-bg{position:absolute;inset:0;background:radial-gradient(circle at 30% 80%,rgba(60,100,20,.35),transparent 55%),radial-gradient(circle at 85% 70%,rgba(60,100,20,.3),transparent 50%)}
.testimonials h2{position:absolute;left:0;width:1200px;top:82px;text-align:center;font-size:33px;color:var(--white)}
.card{position:absolute;top:205px;width:306px;height:198px;border:2px solid var(--white);text-align:center;color:var(--white)}
.avatar{position:absolute;left:50%;top:-41px;transform:translateX(-50%);width:82px;height:82px;border-radius:50%;border:3px solid var(--white);box-shadow:0 2px 6px rgba(0,0,0,.25)}
.avatar-clara{background:radial-gradient(circle at 50% 62%,#e8c4a8 0 30%,transparent 31%),linear-gradient(180deg,#c9a46a 0%,#b38a52 55%,#eef0f2 56%,#dfe3e8 100%)}
.avatar-nora{background:radial-gradient(circle at 50% 58%,#e6bfa4 0 30%,transparent 31%),linear-gradient(180deg,#8a8f96 0%,#6e737a 50%,#3f4a5a 51%,#2d3645 100%)}
.avatar-owen{background:radial-gradient(circle at 50% 58%,#d6a98a 0 30%,transparent 31%),linear-gradient(180deg,#3a2e28 0%,#4a3a30 45%,#c9ced6 46%,#e4e7eb 100%)}
.card blockquote{margin:64px 28px 0;font-style:italic;font-size:13.5px;line-height:24px}
.card cite{display:block;margin-top:10px;font-style:normal;font-family:"Montserrat",sans-serif;font-weight:600;font-size:18px}
.arrow{position:absolute;top:282px}

/* Footer */
.footer-brand{position:absolute;left:95px;top:3160px;font-family:"Montserrat",sans-serif;font-weight:700;font-size:44px;color:var(--ink);letter-spacing:1px}
.footer-col{position:absolute;top:3092px}
.footer-col h4{font-family:"Montserrat",sans-serif;font-weight:700;font-size:16px;color:var(--ink);margin-bottom:18px}
.links li{list-style:none;font-size:12px;line-height:24.5px;color:var(--ink)}
.newsletter p{font-size:12px;line-height:20px;color:var(--ink);width:260px}
.email-field{margin-top:14px;width:255px;border-bottom:1px solid #bbb;font-size:11.5px;color:#999;padding-bottom:8px}
.btn-sub{margin-top:22px;width:102px;height:34px;border-radius:17px;background:var(--green);color:var(--white);font-family:"Montserrat",sans-serif;font-weight:600;font-size:11px;display:flex;align-items:center;justify-content:center}
.contact li{list-style:none;font-size:12px;line-height:16px;color:var(--ink);display:flex;gap:12px;margin-bottom:14px}
.contact svg{flex:none;margin-top:1px}
.footer-rule{position:absolute;left:100px;top:3326px;width:1000px;height:1px;background:#ddd}
.copyright{position:absolute;left:100px;top:3362px;font-size:12px;color:var(--ink)}
.social{position:absolute;left:927px;top:3351px;display:flex;gap:10px}
.social-link{width:34px;height:34px;border-radius:50%;border:1.5px solid var(--blue);display:flex;align-items:center;justify-content:center}
</style>
</head>
<body>

<header class="hero">
  <div class="hero-photo" role="img" aria-label="Oil refinery towers at dusk"></div>
  <div class="hero-shade"></div>
  <div class="topbar">
    <span><svg width="14" height="14" viewBox="0 0 24 24"><path fill="#acd036" d="M6.6 10.8a15.1 15.1 0 0 0 6.6 6.6l2.2-2.2a1 1 0 0 1 1-.25 11.4 11.4 0 0 0 3.6.57 1 1 0 0 1 1 1V20a1 1 0 0 1-1 1A17 17 0 0 1 3 4a1 1 0 0 1 1-1h3.5a1 1 0 0 1 1 1c0 1.250.2 2.45.57 3.57a1 1 0 0 1-.25 1z"/></svg>1 800 555 0142</span>
    <span class="sep"></span>
    <span><svg width="15" height="12" viewBox="0 0 24 18"><rect width="24" height="18" rx="2" fill="#acd036"/><path d="M2 3l10 7 10-7" stroke="#fff" stroke-width="2" fill="none"/></svg>info@norvane.com</span>
  </div>
  <div class="brand">NORVANE</div>
  <nav class="nav">
    <span class="active">HOME</span><span>ABOUT US</span><span>SOLUTIONS</span><span>TECHNOLOGY</span><span>BLOG</span><span>CONTACT US</span>
    <svg width="16" height="16" viewBox="0 0 24 24"><circle cx="10" cy="10" r="7" stroke="#fff" stroke-width="3" fill="none"/><path d="M15 15l6 6" stroke="#fff" stroke-width="3"/></svg>
  </nav>
  <h1 class="heading hero-title">CLOUD SOFTWARE<br>SOLUTIONS FOR<br>OILFIELD</h1>
  <div class="btn-demo">SCHEDULE A DEMO</div>
  <div class="slider-dots"><i class="on"></i><i></i><i></i><i></i></div>
</header>

<h2 class="heading section-title mission-title">OUR MISSION</h2>
<p class="mission-text">Connect every field equipment and worker including back office to provide a seamless connected field operation. Reduce operational spending without upfront capital investment. Provide self-learning digital solutions at every step of the way assisting.</p>
<div class="video">
  <div class="video-still" role="img" aria-label="Offshore oil platform at sunset"></div>
  <svg class="play" width="40" height="44" viewBox="0 0 40 44"><path d="M4 2l34 20L4 42z" fill="#fff"/></svg>
</div>

<section class="industry">
  <div class="industry-panel"></div>
  <div class="industry-photo" role="img" aria-label="Industrial plant with smokestacks under a hazy sky"></div>
  <h2 class="heading">INDUSTRY SOLUTIONS</h2>
  <p>We offer solutions for wide variety of industries such as oil &amp; gas, industrial, health safety and environment (HSE) with an in-depth knowledge and experience of and back office flow information for oil &amp; gas industry which significantly reduces the cost of operations. We have in-depth knowledge and experience when it comes to servicing equipment's, tracking personnel and inventory for industrial machines. The solutions cater to predictive behavior rather than being reactive. We have in-depth knowledge and experience on avoiding safety incidents and managing site inspection lifecycles.</p>
  <div class="btn-outline">READ MORE</div>
</section>

<h2 class="heading section-title tech-title">TECHNOLOGY</h2>
<p class="tech-text">We offer disruptive technology to connect field services, data collection using IoT, monitor assets in the field, automated feed from analysis results, automated workflows, integrate with enterprise systems, RFID, GPS asset tracking and process high volume data for analysis using big data technology. We mobilize field workers using mobile platforms, cloud technology for servicing, monitoring and prescribing.</p>

<svg class="diagram" width="1200" height="2500" viewBox="0 0 1200 2500" aria-label="Technology capabilities">
  <g stroke="#0a2a6b" stroke-width="1.5">
    <line x1="588" y1="2183" x2="584" y2="2014"/><line x1="588" y1="2183" x2="468" y2="2071"/>
    <line x1="588" y1="2183" x2="703" y2="2071"/><line x1="588" y1="2183" x2="411" y2="2183"/>
    <line x1="588" y1="2183" x2="760" y2="2183"/><line x1="588" y1="2183" x2="468" y2="2300"/>
    <line x1="588" y1="2183" x2="703" y2="2300"/><line x1="588" y1="2183" x2="584" y2="2354"/>
  </g>
  <circle cx="588" cy="2183" r="91" fill="#0a2a6b"/>
  <text x="588" y="2195" text-anchor="middle" style="font-family:Montserrat,sans-serif;font-weight:700;font-size:32px;fill:#fff">NORVANE</text>
  <g fill="#8cc63f">
    <circle cx="584" cy="2014" r="43"/><circle cx="468" cy="2071" r="43"/><circle cx="703" cy="2071" r="43"/>
    <circle cx="411" cy="2183" r="43"/><circle cx="760" cy="2183" r="43"/><circle cx="468" cy="2300" r="43"/>
    <circle cx="703" cy="2300" r="43"/><circle cx="584" cy="2354" r="43"/>
  </g>
  <g fill="#fff" stroke="#fff">
    <path d="M566 2026h38a10 10 0 0 0 0-20 14 14 0 0 0-27-4 11 11 0 0 0-11 24z" stroke="none"/>
    <g fill="none" stroke-width="4"><path d="M450 2060h10l16 22h12M450 2082h10l16-22h12"/><path d="M482 2054l7 6-7 6M482 2076l7 6-7 6" stroke-width="3"/></g>
    <g fill="none" stroke-width="4"><path d="M696 2058a14 14 0 0 1 0 26M710 2084a14 14 0 0 1 0-26"/></g>
    <rect x="400" y="2163" width="22" height="40" rx="3" fill="none" stroke-width="3"/><circle cx="411" cy="2197" r="2" stroke="none"/>
    <g fill="none" stroke-width="4"><path d="M744 2178a22 22 0 0 1 32 0M749 2185a14 14 0 0 1 22 0"/></g><circle cx="760" cy="2194" r="3.5" stroke="none"/>
    <g stroke="none"><rect x="452" y="2302" width="7" height="14"/><rect x="463" y="2296" width="7" height="20"/><rect x="474" y="2290" width="7" height="26"/></g>
    <path d="M450 2296l12-10 8 5 16-14" fill="none" stroke-width="3"/>
    <g stroke="none"><rect x="687" y="2306" width="6" height="12"/><rect x="696" y="2298" width="6" height="20"/><rect x="705" y="2290" width="6" height="28"/><rect x="714" y="2282" width="6" height="36"/></g>
    <rect x="566" y="2338" width="36" height="32" fill="none" stroke-width="3"/><path d="M570 2362l9-10 8 6 11-12" fill="none" stroke-width="3"/>
  </g>
  <text x="584" y="1961" text-anchor="middle">Cloud Platform</text>
  <text x="414" y="2068" text-anchor="end">API &amp; Integration</text>
  <text x="758" y="2067">Automated &amp;</text><text x="758" y="2088">Configurable Workflows</text>
  <text x="354" y="2190" text-anchor="end">Mobile Platform</text>
  <text x="820" y="2183">RFID &amp; GPS</text><text x="820" y="2203">Technology</text>
  <text x="398" y="2309" text-anchor="end">Big Data</text>
  <text x="756" y="2309">IoT Ready</text>
  <text x="584" y="2422" text-anchor="middle">Analytics / ML / AI</text>
</svg>

<section class="testimonials">
  <div class="testimonials-bg" role="img" aria-label="Aerial view of an industrial facility tinted green"></div>
  <h2 class="heading">TESTIMONIALS</h2>
  <svg class="arrow" style="left:24px" width="44" height="44" viewBox="0 0 44 44"><circle cx="22" cy="22" r="20" stroke="#fff" stroke-width="2" fill="none"/><path d="M25 14l-8 8 8 8" stroke="#fff" stroke-width="2.5" fill="none"/></svg>
  <svg class="arrow" style="left:1130px" width="44" height="44" viewBox="0 0 44 44"><circle cx="22" cy="22" r="20" stroke="#fff" stroke-width="2" fill="none"/><path d="M19 14l8 8-8 8" stroke="#fff" stroke-width="2.5" fill="none"/></svg>
  <div class="card" style="left:100px"><div class="avatar avatar-clara" role="img" aria-label="Portrait photo of Clara Westin"></div>
    <blockquote>Nam libero tempore, cum soluta nobis est eligendi optio cumque nihil impedit quo minus id quod maxime placea<cite>Clara Westin</cite></blockquote></div>
  <div class="card" style="left:447px"><div class="avatar avatar-nora" role="img" aria-label="Portrait photo of Nora Hadley"></div>
    <blockquote>Nam libero tempore, cum soluta nobis est eligendi optio cumque nihil impedit quo minus id quod maxime placea<cite>Nora Hadley</cite></blockquote></div>
  <div class="card" style="left:794px"><div class="avatar avatar-owen" role="img" aria-label="Portrait photo of Owen Brandt"></div>
    <blockquote>Nam libero tempore, cum soluta nobis est eligendi optio cumque nihil impedit quo minus id quod maxime placea<cite>Owen Brandt</cite></blockquote></div>
</section>

<footer>
  <div class="footer-brand">NORVANE</div>
  <div class="footer-col" style="left:411px">
    <h4>QUICK LINKS</h4>
    <ul class="links"><li>Help</li><li>FAQ</li><li>Support</li><li>Sitemap</li><li>Terms Of Use</li><li>Privacy Statement</li></ul>
  </div>
  <div class="footer-col newsletter" style="left:602px">
    <h4>NEWSLETTER SUBSCRIPTION</h4>
    <p>Register your Email Address to get information about us</p>
    <div class="email-field">Email Address</div>
    <div class="btn-sub">SUBSCRIBE</div>
  </div>
  <div class="footer-col" style="left:919px">
    <h4>CONTACT US</h4>
    <ul class="contact">
      <li><svg width="12" height="14" viewBox="0 0 24 30"><path d="M12 0a10 10 0 0 0-10 10c0 8 10 20 10 20s10-12 10-20A10 10 0 0 0 12 0zm0 14a4 4 0 1 1 0-8 4 4 0 0 1 0 8z" fill="#0255a3"/></svg><span>4120 Ridgeline Parkway<br>Amarillo, TX 79110</span></li>
      <li><svg width="13" height="13" viewBox="0 0 24 24"><path fill="#0255a3" d="M6.6 10.8a15.1 15.1 0 0 0 6.6 6.6l2.2-2.2a1 1 0 0 1 1-.25 11.4 11.4 0 0 0 3.6.57 1 1 0 0 1 1 1V20a1 1 0 0 1-1 1A17 17 0 0 1 3 4a1 1 0 0 1 1-1h3.5a1 1 0 0 1 1 1c0 1.25.2 2.45.57 3.57a1 1 0 0 1-.25 1z"/></svg><span>1 800 555 0142</span></li>
      <li><svg width="14" height="13" viewBox="0 0 24 22"><rect x="0" y="4" width="24" height="18" rx="2" fill="#0255a3"/><rect x="5" y="0" width="14" height="7" fill="#0255a3"/><rect x="4" y="9" width="16" height="3" fill="#fff"/></svg><span>1 800 555 0199</span></li>
      <li><svg width="14" height="11" viewBox="0 0 24 18"><rect width="24" height="18" rx="2" fill="#0255a3"/><path d="M2 3l10 7 10-7" stroke="#fff" stroke-width="2" fill="none"/></svg><span>info@norvane.com</span></li>
    </ul>
  </div>
  <div class="footer-rule"></div>
  <div class="copyright">Copyrights © 2018, Norvane. All rights reserved.</div>
  <div class="social" aria-label="Social links">
    <span class="social-link" aria-label="Share"><svg width="14" height="14" viewBox="0 0 24 24"><circle cx="18" cy="5" r="3" fill="#0255a3"/><circle cx="6" cy="12" r="3" fill="#0255a3"/><circle cx="18" cy="19" r="3" fill="#0255a3"/><path d="M8.6 10.7l6.8-4M8.6 13.3l6.8 4" stroke="#0255a3" stroke-width="2"/></svg></span>
    <span class="social-link" aria-label="Chat"><svg width="14" height="14" viewBox="0 0 24 24"><path d="M3 4h18v12H9l-5 4v-4H3z" fill="#0255a3"/></svg></span>
    <span class="social-link" aria-label="Video"><svg width="14" height="14" viewBox="0 0 24 24"><path d="M7 4l14 8-14 8z" fill="#0255a3"/></svg></span>
    <span class="social-link" aria-label="Link"><svg width="14" height="14" viewBox="0 0 24 24"><path d="M10 14a5 5 0 0 0 7 0l3-3a5 5 0 0 0-7-7l-1 1M14 10a5 5 0 0 0-7 0l-3 3a5 5 0 0 0 7 7l1-1" stroke="#0255a3" stroke-width="2.4" fill="none" stroke-linecap="round"/></svg></span>
  </div>
</footer>

</body>
</html>
```